I want a business card that is going to show a creative spark but without limiting me to an industry. Something edgy but that wont go out of date. I want it state My business name Verity Lanes, profession - Professional Makeup Artist contact number and email

My service is to provide makeup services from bridal, fashion, photography, film, TV and so on. It is creative and different so i want that to be reflected.

I would like the card double sided.
Updates

 I would LOVE a background on my card something like this image... i can supply an image to be formed like this

Please use the image uploaded

Can we try using the image provided on one side of the card and then writing and details on the other side

Target Market(s)

I am targeting a wide range of people from Creative directors to the individual eg. bride

Industry/Entity Type

Business

Requirements
Must have
• Name: Harriet Cole
contact numbe 0417 583 940
email address:info@veritylanes.example
website: www.veritylanes.example
One of the images attached

professional makeup artist / hair stylist

I want it to show creativity
Nice to have
• logo, Double-sided card
Should not have
• the design should not use tradional style. Or images that are not my own

```html
<!DOCTYPE html>
<html lang="en">
<head>
<meta charset="utf-8">
<title>Verity Lanes – Business Card</title>
<link rel="stylesheet" href="https://fonts.googleapis.com/css2?family=Macondo&family=Kalam:wght@300;400&display=swap">
<style>
  :root {
    --navy: #0b1b80;
    --royal: #2f3fa6;
    --mist: #d9dcef;
    --cream: #f6f1ec;
    --ink: #111111;
    --contact: #f4f1ff;
    --page: #ffffff;
  }
  html, body {
    margin: 0;
    padding: 0;
    width: 1200px;
    height: 1200px;
    overflow: hidden;
    background: var(--page);
  }
  .canvas {
    position: relative;
    width: 1200px;
    height: 1200px;
  }
  .card {
    position: absolute;
    width: 767px;
    height: 575px;
    overflow: hidden;
    background: linear-gradient(
      to bottom,
      var(--navy) 0%,
      var(--royal) 14%,
      var(--mist) 23%,
      var(--cream) 27%,
      var(--cream) 70%,
      var(--mist) 74%,
      var(--royal) 84%,
      var(--navy) 100%
    );
  }
  .card--front { left: 25px; top: 15px; }
  .card--back  { left: 424px; top: 604px; border-left: 1px solid #c0303a; }

  .brand-name {
    position: absolute;
    left: 0; right: 0; top: 22px;
    margin: 0;
    text-align: center;
    font-family: "Macondo", cursive;
    font-weight: 400;
    font-size: 100px;
    letter-spacing: 3px;
    color: var(--ink);
    line-height: 1;
  }
  .eye-art {
    position: absolute;
    left: 196px; top: 160px;
    width: 380px; height: 220px;
    border-radius: 48% 52% 40% 60% / 60% 55% 45% 40%;
    background: linear-gradient(200deg, #ffffff 0%, #6f7fd0 30%, var(--royal) 60%, #0a1570 100%);
  }
  .profession {
    position: absolute;
    left: 0; right: 0; top: 395px;
    margin: 0;
    text-align: center;
    font-family: "Kalam", cursive;
    font-weight: 400;
    font-size: 40px;
    color: var(--ink);
    line-height: 1.2;
  }
  .profession span {
    border-bottom: 2px solid var(--ink);
    padding: 0 4px;
  }
  .contact-list {
    position: absolute;
    left: 0; right: 0; top: 458px;
    margin: 0;
    padding: 0;
    list-style: none;
    text-align: center;
    font-family: "Kalam", cursive;
    font-weight: 400;
    font-size: 27px;
    line-height: 37px;
    color: var(--contact);
  }
  .contact-list .label { display: inline-block; margin-right: 18px; }

  .services {
    position: absolute;
    left: 0; right: 0; top: 28px;
    margin: 0;
    padding: 0;
    list-style: none;
    text-align: center;
    font-family: "Macondo", cursive;
    font-size: 38px;
    color: var(--ink);
    line-height: 49px;
  }
  .services .services-title { font-size: 37px; }
  .lips-art {
    position: absolute;
    left: 190px; top: 325px;
    width: 390px; height: 225px;
    border-radius: 50% 50% 46% 46% / 44% 44% 56% 56%;
    background: radial-gradient(ellipse at 50% 40%, #f2f2f2 0%, #9a9a9a 35%, #222222 65%, #1a2a8c 100%);
  }
</style>
</head>
<body>
<main class="canvas">
  <section class="card card--front" aria-label="Card front">
    <h1 class="brand-name">Verity Lanes</h1>
    <div class="eye-art" role="img" aria-label="Illustration of a closed eye with blue eyeshadow and long lashes"></div>
    <p class="profession"><span>Professional Make up Artist</span></p>
    <ul class="contact-list">
      <li class="contact contact--phone"><span class="label">Phone:</span>0417 583 940</li>
      <li class="contact contact--email"><span class="label">e-mail:</span>info@veritylanes.example</li>
      <li class="contact contact--web"><span class="label">web:</span>www.veritylanes.example</li>
    </ul>
  </section>

  <section class="card card--back" aria-label="Card back">
    <ul class="services">
      <li class="services-title">Make up Services include:</li>
      <li>Wedding</li>
      <li>Fashion</li>
      <li>Photography</li>
      <li>Film</li>
      <li>Television</li>
    </ul>
    <div class="lips-art" role="img" aria-label="Painted illustration of lips in black and white ink"></div>
  </section>
</main>
</body>
</html>
```